Supplement Company Needs a Label Design

We need a label design for our pre-workout tub. Our company name is Quarry Athletics, we would like to emphasize the product's clinically dosed, science-based, transparent formula. We would like the label to mention our slogan "Iron Sharpens Iron." We would like you to experiment with colors and color schemes; the photo included is colorful, but that's not necessarily what we are looking for. We would like our main font & color scheme to match our theme of grittiness and boldness. We would like you to include how it boosts energy, enhances focus, creates bigger pumps, and elongates endurance. (Preferably on the back written vertically aside the supplement facts.) Photo 1 (Plume) is the guideline for the overall idea of what the pre-workout should look like, excluding color scheme and font. Photo 2(Redline Nutrition) is how we'd like to present the energy, focus, pumps, & endurance. This label shows the ingredients next to the supplement facts, however we'd like to show the boosted energy, enhanced focus, bigger pumps, and elongated endurance. The final design should communicate boldness, grit, but we would like it to remain uncluttered and clean looking.

Target Market(s)

Our target market is primarily males who workout in the gym.

Font styles to use
Other font styles liked:
• Blanka

Requirements
Nice to have
• Can incorporate the logo attached if you would like.

```html
<!DOCTYPE html>
<html lang="en">
<head>
<meta charset="UTF-8">
<title>Quarry Athletics Pre-Workout Label</title>
<link href="https://fonts.googleapis.com/css2?family=Orbitron:wght@700;900&family=Exo+2:wght@600;700;800&display=swap" rel="stylesheet">
<style>
  :root {
    --page: #ececec;
    --ink: #0d0d0e;
    --label-black: #141415;
    --deep-red: #3a0a10;
    --mid-red: #6e1420;
    --silver: #dcdde0;
    --white: #ffffff;
  }
  * { margin: 0; padding: 0; box-sizing: border-box; }
  html, body {
    width: 1200px; height: 900px; overflow: hidden;
    background: var(--page);
    font-family: "Exo 2", sans-serif;
  }
  .label {
    position: absolute; left: 100px; top: 150px;
    width: 1000px; height: 600px;
    background: var(--label-black);
    overflow: hidden;
  }
  .stripe-band { position: absolute; left: 0; top: 0; width: 1000px; height: 44px; }
  .field {
    position: absolute; left: 0; top: 44px; width: 1000px; height: 496px;
    background: radial-gradient(ellipse 55% 70% at 50% 45%, var(--mid-red) 0%, var(--deep-red) 55%, var(--label-black) 100%);
  }
  .brand-small {
    position: absolute; top: 76px; width: 100%; text-align: center;
    font-weight: 700; font-size: 26px; letter-spacing: 4px; color: var(--silver);
  }
  .headline {
    position: absolute; width: 100%; text-align: center;
    font-family: "Orbitron", sans-serif; font-weight: 900;
    color: var(--silver); line-height: 1;
  }
  .headline--main { top: 126px; font-size: 100px; letter-spacing: 6px; }
  .headline--sub { top: 238px; font-size: 58px; letter-spacing: 3px; }
  .slogan {
    position: absolute; left: 310px; top: 326px; width: 380px; height: 56px;
    background: var(--silver);
    clip-path: polygon(6% 0, 100% 0, 94% 100%, 0 100%);
    display: flex; align-items: center; justify-content: center;
    font-weight: 800; font-size: 30px; color: var(--ink); letter-spacing: 1px;
  }
  .accent-line { position: absolute; left: 0; top: 0; width: 1000px; height: 600px; pointer-events: none; }
  .servings {
    position: absolute; left: 140px; top: 408px; width: 80px; height: 100px;
    background: var(--white); border-radius: 4px;
    display: flex; flex-direction: column; align-items: center; justify-content: center;
    color: var(--ink);
  }
  .servings__count { font-family: "Orbitron", sans-serif; font-weight: 900; font-size: 40px; line-height: 1; }
  .servings__unit { font-weight: 800; font-size: 14px; margin-top: 4px; }
  .product-type {
    position: absolute; left: 236px; top: 414px;
    font-weight: 800; font-size: 20px; line-height: 1.15; color: var(--silver);
  }
  .benefits { position: absolute; left: 408px; top: 406px; display: flex; gap: 16px; }
  .benefit { width: 76px; text-align: center; color: var(--silver); }
  .benefit svg { width: 56px; height: 62px; display: block; margin: 0 auto; }
  .benefit__name { font-size: 11px; font-weight: 700; margin-top: 4px; letter-spacing: .5px; line-height: 1.2; }
  .nutrition-claims {
    position: absolute; right: 488px; top: 492px; text-align: right;
    font-size: 13px; font-weight: 800; line-height: 1.15; color: var(--silver); letter-spacing: .5px;
  }
  .footer__text {
    position: absolute; left: 0; top: 543px; width: 1000px; text-align: center;
    font-weight: 800; font-size: 20px; line-height: 24px; color: var(--silver); letter-spacing: .5px; word-spacing: 6px;
  }
</style>
</head>
<body>
  <section class="label">
    <svg class="stripe-band" viewBox="0 0 1000 44" aria-hidden="true">
      <defs>
        <pattern id="hazard" width="44" height="44" patternUnits="userSpaceOnUse">
          <polygon points="14,14 34,14 28,30 8,30" fill="#ffffff"/>
        </pattern>
      </defs>
      <rect width="1000" height="44" fill="#141415"/>
      <rect width="1000" height="44" fill="url(#hazard)"/>
    </svg>

    <div class="field"></div>

    <div class="brand-small">QUARRY</div>
    <div class="headline headline--main">QUARRY</div>
    <div class="headline headline--sub">ATHLETICS</div>
    <div class="slogan">IRON SHARPENS IRON</div>

    <svg class="accent-line" viewBox="0 0 1000 600" aria-hidden="true">
      <polyline points="850,330 762,518 520,518" fill="none" stroke="#dcdde0" stroke-width="7"/>
      <line x1="40" y1="555" x2="280" y2="555" stroke="#ffffff" stroke-width="3"/>
      <line x1="720" y1="555" x2="960" y2="555" stroke="#ffffff" stroke-width="3"/>
      <line x1="40" y1="590" x2="960" y2="590" stroke="#ffffff" stroke-width="3"/>
    </svg>

    <div class="servings">
      <span class="servings__count">30</span>
      <span class="servings__unit">SERVING</span>
    </div>
    <div class="product-type">PREWORKOUT<br>ENERGY</div>

    <div class="benefits">
      <div class="benefit">
        <svg viewBox="0 0 56 62" aria-hidden="true">
          <polygon points="28,2 53,16 53,46 28,60 3,46 3,16" fill="#2a2a2c" stroke="#dcdde0" stroke-width="3"/>
          <polygon points="31,14 19,34 27,34 23,48 37,27 29,27" fill="#dcdde0"/>
        </svg>
        <div class="benefit__name">ENERGY</div>
      </div>
      <div class="benefit">
        <svg viewBox="0 0 56 62" aria-hidden="true">
          <polygon points="28,2 53,16 53,46 28,60 3,46 3,16" fill="#2a2a2c" stroke="#dcdde0" stroke-width="3"/>
          <line x1="14" y1="24" x2="30" y2="24" stroke="#dcdde0" stroke-width="3"/>
          <line x1="12" y1="31" x2="34" y2="31" stroke="#dcdde0" stroke-width="3"/>
          <line x1="14" y1="38" x2="30" y2="38" stroke="#dcdde0" stroke-width="3"/>
          <polyline points="34,22 43,31 34,40" fill="none" stroke="#dcdde0" stroke-width="3"/>
        </svg>
        <div class="benefit__name">ALERTNESS</div>
      </div>
      <div class="benefit">
        <svg viewBox="0 0 56 62" aria-hidden="true">
          <polygon points="28,2 53,16 53,46 28,60 3,46 3,16" fill="#2a2a2c" stroke="#dcdde0" stroke-width="3"/>
          <circle cx="28" cy="31" r="12" fill="none" stroke="#dcdde0" stroke-width="2.5"/>
          <circle cx="28" cy="31" r="5" fill="none" stroke="#dcdde0" stroke-width="2.5"/>
          <line x1="28" y1="14" x2="28" y2="48" stroke="#dcdde0" stroke-width="2"/>
          <line x1="11" y1="31" x2="45" y2="31" stroke="#dcdde0" stroke-width="2"/>
        </svg>
        <div class="benefit__name">FOCUS</div>
      </div>
    </div>

    <div class="nutrition-claims">ZERO SUGAR<br>ZERO CALORIES</div>

    <div class="footer__text">DIETARY SUPPLEMENT &nbsp; NET WT. 260 G</div>
  </section>
</body>
</html>
```